依頼詳細
月に1度、製品紹介のPR広告(はがき・ファックス)を配布し、企業のイメージ広告として活用する予定です。配布先のお客様の目を引き、活力があるイメージ広告の作成をお願いいたします。
記載項目
会社名 電話番号  TALK FAX URL
サイズ
A4
ページ数
片面
希望イメージ
シンプル 複雑
単色 カラフル
暗い 明るい
日常 高級
遊び心 厳粛
未来的 伝統的
女性的 男性的
希望する色
黄・オレンジ系、緑系、水色系
納品ファイル
• 高解像度JPG (.jpg)
• イラストレーター形式 (.ai)
補足説明
PR対象商品(エンジン・ラジエーター・コンプレッサー・コンデンサー)の写真をUPしました。

※商品説明などの詳細は不要です。

夏季に発注量が増える商品のため、夏季シーズン限定のデザインとして活用する予定です。
広告を見た方の目に留まり、反応があるデザインを希望しています。

良作が多く悩みましたが、イメージに合致した2点を当選とさせていただきました。

この度は、ご多忙の中、素晴らしいデザインを作成して頂き、誠にありがとうございました。

今後も、同コンペを開催されていただく予定です。今後ともよろしくお願いいたします。

```html
<!DOCTYPE html>
<html lang="ja">
<head>
<meta charset="utf-8">
<title>森川商会 ― Next Stageへ</title>
<link rel="stylesheet" href="https://fonts.googleapis.com/css2?family=Noto+Serif+JP:wght@500;700;900&family=Playfair+Display:ital,wght@1,700&family=Noto+Sans+JP:wght@400;700&display=swap">
<style>
  :root {
    --navy-deep: #06132a;
    --navy: #0f2a52;
    --steel: #3d5878;
    --glow: #5fb8ff;
    --white: #ffffff;
    --ink: #222222;
    --grey: #8a9096;
    --green: #2f8f3e;
    --leaf: #3aa35a;
    --sun: #f2a51c;
    --badge-blue: #1f5fa8;
    --badge-teal: #2aa0a8;
  }
  * { margin: 0; padding: 0; box-sizing: border-box; }
  html, body { width: 849px; height: 1200px; overflow: hidden; background: var(--white); }
  .poster { position: relative; width: 849px; height: 1200px; overflow: hidden; font-family: "Noto Sans JP", sans-serif; }

  .hero-photo {
    position: absolute; left: 0; top: 0; width: 849px; height: 945px;
    background:
      radial-gradient(ellipse at 50% 45%, rgba(95,184,255,0.35), transparent 60%),
      linear-gradient(180deg, var(--steel) 0%, var(--navy) 40%, var(--navy-deep) 100%);
  }
  .hero-heading {
    position: absolute; top: 100px; width: 100%; text-align: center;
    font-family: "Noto Serif JP", serif; font-weight: 900; font-size: 52px;
    color: var(--white); letter-spacing: 2px;
    text-shadow: 0 0 14px var(--glow), 0 0 28px var(--glow);
  }
  .headline {
    position: absolute; width: 100%; text-align: center;
    font-family: "Playfair Display", serif; font-style: italic; font-weight: 700;
    color: var(--white); line-height: 1;
    text-shadow: 0 0 18px var(--glow), 0 0 40px var(--glow), 0 0 70px rgba(95,184,255,0.8);
  }
  .headline-next { top: 270px; font-size: 190px; left: 10px; }
  .headline-stage { top: 425px; font-size: 180px; left: 0; }
  .headline-stage .kana { font-family: "Noto Serif JP", serif; font-style: normal; font-weight: 900; font-size: 140px; }

  .hero-lead {
    position: absolute; top: 668px; width: 100%; text-align: center;
    font-family: "Noto Serif JP", serif; font-weight: 500; font-size: 17px; line-height: 1.6;
    color: var(--white);
  }
  .product-photos { position: absolute; top: 730px; left: 0; width: 849px; height: 195px; }
  .product { position: absolute; top: 0; height: 195px; border-radius: 4px; }
  .product-compressor { left: 40px; width: 150px; background: linear-gradient(160deg, #9aa3ad, #3c434c); }
  .product-radiator { left: 215px; width: 200px; background: linear-gradient(180deg, #c9ced4, #7d858e); }
  .product-engine { left: 450px; width: 340px; background: linear-gradient(150deg, #b6bcc3, #4a5058 70%, #2a2e34); }

  .company-mark { position: absolute; left: 30px; top: 968px; width: 72px; height: 72px; border-radius: 50%; background: var(--leaf); }
  .company-name { position: absolute; left: 118px; top: 964px; font-family: "Noto Serif JP", serif; font-weight: 700; font-size: 44px; color: var(--ink); letter-spacing: 2px; }
  .company-roman { position: absolute; left: 255px; top: 1024px; font-size: 12px; color: var(--ink); letter-spacing: 1px; }
  .address { position: absolute; left: 118px; top: 1062px; font-size: 14px; color: var(--ink); line-height: 1.6; }

  .group-member { position: absolute; left: 535px; top: 985px; display: flex; align-items: center; gap: 8px; }
  .group-member .dot { width: 30px; height: 30px; border-radius: 50%; background: var(--sun); }
  .group-member .name { font-weight: 700; font-size: 22px; color: var(--green); }
  .group-member .note { font-size: 14px; color: var(--ink); }

  .contact-icons { position: absolute; left: 535px; top: 1068px; display: flex; align-items: center; gap: 14px; }
  .talk-account { display: flex; align-items: center; gap: 6px; }
  .talk-account .dot { width: 20px; height: 20px; border-radius: 50%; background: var(--grey); }
  .talk-account .name { font-weight: 700; font-size: 16px; color: var(--ink); }
  .badge { width: 56px; height: 56px; }
  .badge-round { border-radius: 50%; background: var(--badge-teal); }
  .badge-square { background: var(--badge-blue); }

  .phone-line { position: absolute; left: 30px; top: 1140px; font-weight: 700; font-size: 30px; color: var(--green); letter-spacing: 1px; }
  .phone-line .label { font-size: 24px; }
  .phone-line .gap { display: inline-block; width: 26px; }
</style>
</head>
<body>
<div class="poster">
  <section class="hero">
    <div class="hero-photo" role="img" aria-label="自動車エンジン内部の部品を青く照らした写真"></div>
    <h2 class="hero-heading">愛着ある自動車を</h2>
    <h1>
      <span class="headline headline-next">Next</span>
      <span class="headline headline-stage">Stage<span class="kana">へ</span></span>
    </h1>
    <p class="hero-lead">RPNA独自の厳しい品質基準をクリアした全国200万点の中から<br>高品質のリサイクルパーツ・リビルトパーツを販売しています</p>
    <div class="product-photos">
      <div class="product product-compressor" role="img" aria-label="コンプレッサーの写真"></div>
      <div class="product product-radiator" role="img" aria-label="ラジエーターの写真"></div>
      <div class="product product-engine" role="img" aria-label="エンジンの写真"></div>
    </div>
  </section>

  <footer class="company">
    <div class="company-mark"></div>
    <div class="company-name">株式会社 森川商会</div>
    <div class="company-roman">MORIKAWA CO.,LTD</div>
    <p class="address">〒650-0000 兵庫県神戸市中央区架空町1丁目2-3<br>http://www.example-morikawa.jp/index.html</p>

    <div class="group-member">
      <span class="dot"></span><span class="name">RPNA</span><span class="note">グループに加盟しています</span>
    </div>

    <div class="contact-icons">
      <div class="talk-account"><span class="dot"></span><span class="name">TALK</span></div>
      <div class="badge badge-round"></div>
      <div class="badge badge-square"></div>
    </div>

    <p class="phone-line"><span class="label">TEL.</span> 078-000-1234<span class="gap"></span><span class="label">FAX.</span> 078-000-1235</p>
  </footer>
</div>
</body>
</html>
```